依頼詳細
【デザインテイストについて】
カジュアル・ゴージャス・にぎやか・ナチュラル・優しい・パステル
シンプル・清潔な・重厚感

【デザインカラーについて】
サロンの内装にレンガがあるのですが、私が直接施工してまして
それはもし可能であれば、サイトのデザイン内に組み込んで頂ければ
とても嬉しいです。

【参考にしているデザイン】
インテリア本:Hearth Leaf Digest
本内のデザインや見せ方が好みです。
https://hearthleaf.jp/cp/hearthleafdigest

【その他】
●「http://morvelin-salon.com/」のページ下部にあるlinkora部分の様に
サイトの中に挿入したいと考えています。
見本で構いませんので、画像で貼り付けて頂ければ嬉しいです。

●ルナリボンに飛ばす物も良ければ配置してほしいです。

【ページ項目】
①トップページ
②サロン紹介
③スタッフ紹介
④お知らせ
⑤ブログ
⑥スタイルギャラリー
⑦コンセプト
⑧商品紹介
⑨よくある質問
⑩メニュー
⑪クーポン
⑫フリーマーケット
⑬レビュー投稿(お問い合わせのフォーム)
⑭お客様の声

サイトURL
http://beauty.lunaribbon.jp/slnK000584127/
ページ数
1ページ
希望イメージ
シンプル 複雑
単色 カラフル
暗い 明るい
日常 高級
遊び心 厳粛
未来的 伝統的
女性的 男性的
希望する色
ベージュ、グリーン、茶色
納品ファイル
• 高解像度JPG (.jpg)
• イラストレーター形式 (.ai)
• フォトショップ形式 (.psd)
• PNG形式 (.png)
補足説明
----------------------------------------------------

【素材について】
※ロゴ
サロンのキャラクターがあるので、サイトの中で使って頂ければ幸いです。
http://filevaultbox.jp/download/9a3e7c10bd4f2a6695e0c7d81f4b2e07a6c9d315
ダウンロードパスワード:qzt4mu8r

※サロン写真
http://filevaultbox.jp/download/2c8b5f1e9d7a3064b1e2f8c5a9d0e7b3c4f6a821
ダウンロードパスワード:wld3pvoe

※その他
イメジオ「https://jp.imegio.com/」の定期契約内の画像は使用可能です。
イメジオ以外は無料の素材をご使用くださいませ。

ゴールデンウィーク中で大変申し訳ありませんが、一週間延長させて頂きます。
是非宜しくお願い致します。
■ 選んだ理由

一目ぼれしました!
とても目を引くデザインで、当サロンのイラストをうまく取り込んで頂いていルなと思い、選ばせて頂きました!

■ 提案者全員のお礼・コメント

沢山のご提案をして頂き、本当にありがとうございました!
とても嬉しく全てのデザインを使用したいところですが、コンペ形式にて1つしか選べないと言うのあとても心苦しく思っています。

またこのような機会がありましたら、ご協力頂けますと幸いです。
ありがとうございました。

```html
<!DOCTYPE html>
<html lang="ja">
<head>
<meta charset="utf-8">
<title>Lumé | Hair and Life</title>
<link href="https://fonts.googleapis.com/css2?family=Noto+Sans+JP:wght@400;500;700&family=Cormorant+Garamond:wght@500;600&family=Great+Vibes&family=Josefin+Sans:wght@400;600;700&display=swap" rel="stylesheet">
<style>
:root{
  --brown:#6b5344;
  --brown-dark:#4a3a30;
  --text:#5a4a40;
  --muted:#9a8a80;
  --pink:#f8dccf;
  --pink-deep:#f0c6b5;
  --cream:#f5f1ed;
  --blush:#f5e7e0;
  --line:#e2d6cf;
  --white:#ffffff;
  --green:#8aa36e;
}
*{margin:0;padding:0;box-sizing:border-box}
html,body{width:1200px;height:3688px;overflow:hidden}
body{position:relative;background:var(--white);color:var(--text);font-family:"Noto Sans JP",sans-serif}
.abs{position:absolute}
.section{position:absolute;left:0;width:1200px}
.ph{position:absolute}

/* header */
.header{top:0;height:140px;background:var(--white)}
.brand{left:40px;top:34px;display:flex;align-items:center;gap:12px}
.brand-dot{width:34px;height:34px;border-radius:50%;background:var(--brown)}
.brand-name{font-family:"Cormorant Garamond",serif;font-weight:600;font-size:40px;line-height:1;color:var(--brown)}
.gnav{left:300px;top:56px;display:flex}
.gnav a{display:block;width:100px;text-align:center;text-decoration:none;color:var(--brown-dark);border-left:1px solid var(--line)}
.gnav a:last-child{border-right:1px solid var(--line)}
.gnav b{display:block;font-family:"Josefin Sans",sans-serif;font-weight:600;font-size:14px;letter-spacing:1px}
.gnav small{display:block;font-size:9px;color:var(--muted);margin-top:3px}
.hours{right:40px;top:14px;font-size:9px;color:var(--muted);text-align:right;line-height:1.4}
.tel{right:40px;top:42px;font-family:"Cormorant Garamond",serif;font-size:30px;line-height:1;color:var(--brown-dark);display:flex;align-items:center;gap:8px;white-space:nowrap}
.reserve{right:40px;top:82px;width:126px;height:28px;background:var(--brown);color:var(--white);font-family:"Josefin Sans",sans-serif;font-size:12px;letter-spacing:2px;display:flex;align-items:center;justify-content:center}

/* hero */
.hero{top:140px;height:640px;background:linear-gradient(180deg,#fbe6dc,var(--pink))}
.hero-photo{left:700px;top:0;width:440px;height:640px;background:linear-gradient(160deg,#f6d2c2,#e9b9a3 60%,#f4dccf)}
.hero-copy{left:300px;top:200px;width:420px;text-align:center;color:var(--white)}
.hero-sub{font-family:"Josefin Sans",sans-serif;font-size:18px;letter-spacing:6px;font-weight:600}
.hero-title{font-family:"Josefin Sans",sans-serif;font-size:84px;font-weight:700;letter-spacing:10px;line-height:1.1;margin-top:10px}
.hero-jp{font-size:22px;letter-spacing:4px;margin-top:6px;font-weight:500}

/* shared headings */
.eyebrow{font-family:"Josefin Sans",sans-serif;font-size:10px;letter-spacing:3px;color:var(--muted);text-align:center}
.script{font-family:"Great Vibes",cursive;font-size:52px;font-weight:400;color:var(--brown);text-align:center;line-height:1.2;margin-top:8px}
.rule{width:60px;height:1px;background:var(--brown);margin:8px auto 0}
.btn-more{position:absolute;width:200px;height:40px;background:var(--brown);color:var(--white);font-family:"Josefin Sans",sans-serif;font-size:13px;letter-spacing:3px;display:flex;align-items:center;justify-content:center}
.head{position:absolute;left:0;width:1200px}

/* concept */
.concept{top:780px;height:340px;background:var(--cream)}
.concept-lead{font-size:16px;letter-spacing:3px;text-align:center;margin-top:20px}
.concept-body{font-size:12px;line-height:2.6;letter-spacing:2px;text-align:center;margin-top:14px}

/* gallery */
.gallery{top:1120px;height:640px;background:var(--blush)}
.style-card{position:absolute;top:180px;width:204px}
.style-img{height:200px}
.style-cap{font-size:11px;color:var(--text);margin-top:12px;line-height:1.6;border-bottom:1px solid var(--line);padding-bottom:6px}

/* news */
.news{top:1760px;height:380px;background:#f1e4dd}
.news-list{position:absolute;left:180px;top:180px;width:840px;list-style:none}
.news-list li{display:flex;gap:24px;align-items:center;height:46px;border-bottom:1px solid var(--line);font-size:12px}
.news-date{font-family:"Josefin Sans",sans-serif;color:var(--brown);display:flex;align-items:center;gap:8px;white-space:nowrap}
.news-date::before{content:"";width:6px;height:6px;background:var(--brown)}
.news-more{right:180px;top:336px;font-family:"Josefin Sans",sans-serif;font-size:11px;color:var(--brown);letter-spacing:1px}

/* product */
.product{top:2140px;height:420px}
.product-photo{left:0;top:0;width:1200px;height:420px;background:linear-gradient(90deg,#8b6a52 0%,#c7ad95 30%,#efe6dc 50%,#dfe7cf 72%,#6f8d52 100%)}
.product-card{left:430px;top:50px;width:340px;height:310px;background:var(--white);outline:1px solid var(--line);outline-offset:-10px;text-align:center;padding-top:30px}
.product-text{font-size:12px;line-height:2.2;letter-spacing:1.5px;margin-top:14px}

/* recommended */
.recommend{top:2560px;height:310px;background:var(--white)}
.banner{position:absolute;top:178px;width:160px;height:110px}
.arrow{position:absolute;top:218px;width:30px;height:30px;border-radius:50%;background:var(--brown-dark);display:flex;align-items:center;justify-content:center}

/* access */
.access{top:2870px;height:570px;background:var(--cream)}
.shop-card{left:170px;top:80px;width:420px;height:420px;background:var(--white);padding:26px 28px}
.shop-title{display:flex;align-items:center;gap:10px;font-size:16px;font-weight:700;color:var(--brown-dark)}
.shop-title i{width:22px;height:22px;border-radius:50%;background:var(--brown);display:block}
.shop-info{font-size:11px;line-height:1.9;margin-top:18px}
.shop-map{position:absolute;left:28px;top:230px;width:364px;height:160px;background:linear-gradient(135deg,#e8e6e1,#d9d6cf)}
.feed{left:720px;top:70px;width:210px;height:440px;background:var(--white);border:1px solid var(--line);padding:12px}
.feed-head{display:flex;align-items:center;gap:8px;font-size:11px;font-weight:700;color:var(--brown-dark)}
.feed-head i{width:26px;height:26px;background:var(--brown);display:block}
.feed-text{font-size:10px;line-height:1.7;margin-top:12px}
.feed-img{margin-top:12px;height:170px;background:linear-gradient(160deg,#cfd3d6,#9ea7a6)}
.partner{left:960px;top:470px;display:flex;align-items:center;gap:10px}
.partner small{font-size:9px;line-height:1.4;color:var(--text)}
.partner span{width:78px;height:28px;background:#e6a2b4;display:block}

/* footer */
.fnav{top:3440px;height:60px;background:#f3e3dc;display:flex;align-items:center;justify-content:center}
.fnav a{font-family:"Josefin Sans",sans-serif;font-size:11px;letter-spacing:1px;color:var(--brown-dark);text-decoration:none;padding:0 12px;border-left:1px solid var(--muted)}
.fnav a:first-child{border-left:none}
.brick{top:3500px;height:188px;background:linear-gradient(180deg,#d9b7a3,#c79a82)}
</style>
</head>
<body>

<header class="section header">
  <div class="abs brand"><span class="brand-dot"></span><span class="brand-name">Lumé</span></div>
  <nav class="abs gnav">
    <a href="#"><b>NEWS</b><small>お知らせ</small></a>
    <a href="#"><b>CONCEPT</b><small>コンセプト</small></a>
    <a href="#"><b>MENU</b><small>メニュー</small></a>
    <a href="#"><b>STYLE</b><small>スタイル</small></a>
    <a href="#"><b>STAFF</b><small>スタッフ</small></a>
    <a href="#"><b>PRODUCT</b><small>商品紹介</small></a>
  </nav>
  <div class="abs hours">Weekdays 10:00-19:00<br>Regular holiday Wednesday</div>
  <div class="abs tel">
    <svg width="16" height="16" viewBox="0 0 24 24"><path fill="#6b5344" d="M6.6 10.8a15 15 0 0 0 6.6 6.6l2.2-2.2a1 1 0 0 1 1-.25 11.4 11.4 0 0 0 3.6.57 1 1 0 0 1 1 1V20a1 1 0 0 1-1 1A17 17 0 0 1 3 4a1 1 0 0 1 1-1h3.5a1 1 0 0 1 1 1c0 1.25.2 2.45.57 3.57a1 1 0 0 1-.25 1z"/></svg>
    042-518-2946
  </div>
  <div class="abs reserve">RESERVE</div>
</header>

<section class="section hero">
  <div class="ph hero-photo" role="img" aria-label="Smiling woman with long brown hair, hands on cheeks"></div>
  <div class="abs hero-copy">
    <p class="hero-sub">HAIR AND LIFE</p>
    <h1 class="hero-title">BEAUTY</h1>
    <p class="hero-jp">もっときれいになろう</p>
  </div>
</section>

<section class="section concept">
  <div class="head" style="top:34px">
    <p class="eyebrow">CONCEPT</p>
    <h2 class="script">Concept</h2>
    <div class="rule"></div>
    <p class="concept-lead">ここにテキストが入ります</p>
    <p class="concept-body">ここにテキストが入りますここにテキストが入りますここにテキストが入ります<br>ここにテキストが入りますここにテキストが入りますここにテキストが入りますここにテキストが入ります<br>ここにテキストが入りますここにテキストが入りますここにテキストが入ります</p>
  </div>
</section>

<section class="section gallery">
  <div class="head" style="top:44px">
    <p class="eyebrow">HAIR STYLE</p>
    <h2 class="script">Style Gallery</h2>
    <div class="rule"></div>
  </div>
  <div class="style-card" style="left:168px"><div class="ph style-img" style="position:relative;background:linear-gradient(160deg,#e8d3c6,#b48e76)" role="img" aria-label="Woman with soft wavy bob"></div><p class="style-cap">ふんわり軽やかなミディアムボブ</p></div>
  <div class="style-card" style="left:444px"><div class="ph style-img" style="position:relative;background:linear-gradient(160deg,#efe0d2,#c9a27c)" role="img" aria-label="Woman with light blonde short cut"></div><p class="style-cap">透け感カラーのショートスタイル</p></div>
  <div class="style-card" style="left:720px"><div class="ph style-img" style="position:relative;background:linear-gradient(160deg,#ece2dc,#8e6a55)" role="img" aria-label="Woman with curly medium hair"></div><p class="style-cap">ゆるふわカールのセミロング</p></div>
  <div class="style-card" style="left:996px;width:180px"><div class="ph style-img" style="position:relative;background:linear-gradient(160deg,#d9d2c9,#5c4a3e)" role="img" aria-label="Man with long wavy hair and beard"></div><p class="style-cap">大人のメンズロングスタイル</p></div>
  <div class="btn-more" style="left:500px;top:440px">MORE</div>
</section>

<section class="section news">
  <div class="head" style="top:44px">
    <p class="eyebrow">INFORMATION</p>
    <h2 class="script">Lumé News</h2>
    <div class="rule"></div>
  </div>
  <ul class="news-list">
    <li><span class="news-date">2016.04.20</span><span>テキストが入りますテキストが入りますテキストが入りますテキストが入ります</span></li>
    <li><span class="news-date">2016.04.20</span><span>テキストが入りますテキストが入りますテキストが入りますテキストが入ります</span></li>
    <li><span class="news-date">2016.04.20</span><span>テキストが入りますテキストが入りますテキストが入りますテキストが入ります</span></li>
  </ul>
  <p class="abs news-more">more ›</p>
</section>

<section class="section product">
  <div class="ph product-photo" role="img" aria-label="Salon interior with a brown leather chair and green plants"></div>
  <div class="abs product-card">
    <p class="eyebrow">SALON ITEM</p>
    <h2 class="script">Product</h2>
    <div class="rule"></div>
    <p class="product-text">ここにテキストが入りますここにテキスト<br>ここにテキストが入りますここにテキスト</p>
    <div class="btn-more" style="left:70px;top:236px">MORE</div>
  </div>
</section>

<section class="section recommend">
  <div class="head" style="top:36px">
    <p class="eyebrow">PICK UP</p>
    <h2 class="script">Recommended</h2>
    <div class="rule"></div>
  </div>
  <div class="arrow" style="left:130px"><svg width="10" height="12" viewBox="0 0 10 12"><path d="M8 1 2 6l6 5" stroke="#fff" stroke-width="2" fill="none"/></svg></div>
  <div class="banner" style="left:172px;background:linear-gradient(135deg,#9fc3c9,#e9c7c0)" role="img" aria-label="Campaign banner with salon goods"></div>
  <div class="banner" style="left:346px;background:linear-gradient(135deg,#3b332e,#8a7466)" role="img" aria-label="Hair product bottles banner"></div>
  <div class="banner" style="left:520px;background:linear-gradient(135deg,#cdd6cf,#f1efe9)" role="img" aria-label="Salon space banner"></div>
  <div class="banner" style="left:694px;background:linear-gradient(135deg,#d9356f,#f07aa0)" role="img" aria-label="Pink coupon banner"></div>
  <div class="banner" style="left:868px;background:linear-gradient(135deg,#f6e6c8,#f2c6c0)" role="img" aria-label="Pastel event banner"></div>
  <div class="arrow" style="left:1040px"><svg width="10" height="12" viewBox="0 0 10 12"><path d="M2 1l6 5-6 5" stroke="#fff" stroke-width="2" fill="none"/></svg></div>
</section>

<section class="section access">
  <div class="abs shop-card">
    <p class="shop-title"><i></i>Lumé アンドルミエ 店舗情報</p>
    <p class="shop-info">東京都町田市中町一丁目 5-2 ルミエビル 2F<br>駅から徒歩5分<br>営業時間：10:00〜19:00（最終受付 18:00）<br>定休日：毎週水曜日<br>電話番号：042-518-2946</p>
    <div class="shop-map" role="img" aria-label="Street map around the salon"></div>
  </div>
  <div class="abs feed">
    <p class="feed-head"><i></i>Lumé アンドルミエ</p>
    <p class="feed-text">linkora ページ 最新投稿<br>店内の春のディスプレイが新しくなりました。ご来店をお待ちしています。</p>
    <div class="feed-img" role="img" aria-label="Posted photo of a tree near the salon"></div>
    <p class="feed-text">いいね！ ・ コメント ・ シェア</p>
  </div>
  <div class="abs partner"><small>ネット予約は<br>こちらから</small><span role="img" aria-label="ルナリボン booking badge"></span></div>
</section>

<nav class="section fnav">
  <a href="#">NEWS</a><a href="#">CONCEPT</a><a href="#">MENU</a><a href="#">STYLE</a><a href="#">STAFF</a><a href="#">PRODUCT</a><a href="#">COUPON</a><a href="#">REVIEW</a><a href="#">FAQ</a><a href="#">FREE MARKET</a><a href="#">BLOG</a><a href="#">Q&amp;A</a>
</nav>
<div class="section brick" role="img" aria-label="Hand-laid brick wall from the salon interior"></div>

</body>
</html>
```